CD Design Cover - "Beyond the Orchard Gate"

I need a CD cover design. The original Album or CD was recorded in the early eighties. We are re-mastering it. It needs a fresh cover. The genre' is contemporary Christian music and the title of the album is "Beyond the Orchard Gate." This is referring to caring outside of the church walls. A picture of the solo artist could be integrated in the back design. It is not a good picture and does not have to be used. You would have to be creative in using it because of the quality. It does not have to be used at all. I also added some pictures I liked that could be used. I think I like the "Empty church opening" the best. Fits the theme perfectly.

Target Market(s)

30 years old and older.

Requirements
Must have
• Warmth
Nice to have
• I attached two pictures. One of an empty church and one with a reflection of a stain glass window on the wall. It would be nice to see some offerings using these pictures.
Should not have
• Not too churchy

```html
<!DOCTYPE html>
<html lang="en">
<head>
<meta charset="utf-8">
<title>Beyond the Orchard Gate — Dale Harwick</title>
<link rel="stylesheet" href="https://fonts.googleapis.com/css2?family=Comfortaa:wght@700&family=Josefin+Slab:wght@400;600&display=swap">
<style>
  :root {
    --stage: #2e2e2e;
    --plum-deep: #1f0f2e;
    --plum: #4a1e4f;
    --magenta: #9b1f4e;
    --crimson: #b3213f;
    --violet: #7a4aa8;
    --sunset: #f2a03a;
    --amber: #e8782c;
    --ember: #7a2a1e;
    --pew-dark: #2a1412;
    --title-white: #ffffff;
    --title-red: #ff3b4e;
    --text-soft: #f3ecf4;
    --name-warm: #f6d9c4;
    --rim: #e9eef2;
    --rim-edge: #b8c6d2;
  }
  * { box-sizing: border-box; margin: 0; padding: 0; }
  html, body { width: 1200px; height: 600px; overflow: hidden; }
  body {
    background: var(--stage);
    position: relative;
    font-family: "Josefin Slab", Georgia, serif;
    color: var(--text-soft);
  }

  /* ---------- shared panel ---------- */
  .panel {
    position: absolute;
    top: 117px;
    width: 366px;
    height: 366px;
    overflow: hidden;
  }

  /* ---------- back cover ---------- */
  .back-cover { left: 95px; }
  .back-art {
    position: absolute; inset: 0;
    background:
      linear-gradient(180deg, rgba(31,15,46,0.55) 0%, rgba(0,0,0,0) 30%),
      linear-gradient(180deg, var(--plum-deep) 0%, var(--magenta) 38%, var(--violet) 56%, var(--crimson) 72%, var(--plum) 100%);
  }
  .artist-portrait {
    position: absolute;
    left: 50%; top: 22px;
    width: 102px; height: 102px;
    margin-left: -51px;
    border-radius: 50%;
    border: 4px solid #0b0b0b;
    background: radial-gradient(circle at 50% 45%, #c9a48a 0%, #8f6f5e 55%, #3c3a3a 100%);
  }
  .track-list {
    position: absolute;
    left: 0; right: 0; top: 138px;
    list-style: none;
    text-align: center;
    font-size: 12px;
    line-height: 14.3px;
    font-weight: 600;
    letter-spacing: 0.2px;
  }
  .credits-badge {
    position: absolute;
    left: 26px; top: 310px;
    width: 92px; height: 48px;
    background: #e6e4e8;
  }
  .credits {
    position: absolute;
    left: 129px; top: 315px;
    font-size: 6px;
    line-height: 7.4px;
  }
  .credits dt { display: inline-block; width: 38px; }
  .credits dd { display: inline; }
  .credits dd::after { content: ""; display: block; }
  .studio-mark {
    position: absolute;
    left: 251px; top: 310px;
    width: 75px; height: 38px;
    background: #b07a3a;
    border: 1px solid #e7c79a;
    display: flex; align-items: center; justify-content: center;
    font-size: 9px; font-weight: 600;
  }
  .studio-city {
    position: absolute;
    left: 246px; top: 352px;
    width: 85px;
    text-align: center;
    font-size: 6px;
    letter-spacing: 0.4px;
  }

  /* ---------- front cover ---------- */
  .front-cover { left: 472px; z-index: 2; box-shadow: 4px 0 10px rgba(0,0,0,0.45); }
  .front-art {
    position: absolute; inset: 0;
    background:
      radial-gradient(ellipse 34% 30% at 50% 44%, #ffd36a 0%, var(--sunset) 35%, rgba(232,120,44,0) 100%),
      linear-gradient(180deg, var(--plum-deep) 0%, #3a1a3c 22%, var(--amber) 52%, var(--ember) 72%, var(--pew-dark) 100%);
  }
  .album-title {
    position: absolute;
    left: 0; right: 0; top: 24px;
    text-align: center;
    font-family: "Comfortaa", "Trebuchet MS", sans-serif;
    font-weight: 700;
    font-size: 18px;
    line-height: 23px;
    letter-spacing: 0.5px;
    color: var(--title-white);
    text-transform: uppercase;
  }
  .accent { color: var(--title-red); }
  .artist-name {
    position: absolute;
    left: 0; right: 0; bottom: 13px;
    text-align: center;
    font-size: 13px;
    letter-spacing: 0.6px;
    text-transform: uppercase;
    color: var(--name-warm);
  }

  /* ---------- disc ---------- */
  .disc {
    position: absolute;
    left: 751px; top: 129px;
    width: 350px; height: 350px;
    z-index: 1;
  }
  .disc svg { display: block; }
  .disc-title {
    position: absolute;
    left: 0; right: 0; top: 23px;
    text-align: center;
    font-family: "Comfortaa", "Trebuchet MS", sans-serif;
    font-weight: 700;
    font-size: 16px;
    line-height: 20px;
    color: var(--title-white);
    text-transform: uppercase;
  }
  .disc-artist {
    position: absolute;
    left: 0; right: 0; bottom: 28px;
    text-align: center;
    font-size: 13px;
    letter-spacing: 0.5px;
    text-transform: uppercase;
    color: var(--name-warm);
  }
  .disc-catalog {
    position: absolute;
    left: 296px; top: 172px;
    font-family: Arial, sans-serif;
    font-size: 6px;
    color: var(--text-soft);
  }
</style>
</head>
<body>

  <section class="panel back-cover" aria-label="Back cover">
    <div class="back-art" role="img" aria-label="Textured plum, magenta and violet backdrop with horizontal light streaks"></div>
    <div class="artist-portrait" role="img" aria-label="Portrait photo of the artist"></div>
    <ol class="track-list">
      <li>Open Hands Again</li>
      <li>Beyond the Orchard Gate</li>
      <li>Simple Neighbors</li>
      <li>The Road We Walked Along</li>
      <li>Still Here</li>
      <li>A Quiet Word for You</li>
      <li>A Table Prayer</li>
      <li>Back Where I Started</li>
      <li>Grace at the Door</li>
      <li>We Will Gather In</li>
    </ol>
    <div class="credits-badge" aria-hidden="true"></div>
    <dl class="credits">
      <dt>Producer :</dt><dd>Nora Pell</dd>
      <dt>Engineered :</dt><dd>Glen Marsh</dd>
      <dt>Recorded at :</dt><dd>Cedar Hollow Studio</dd>
      <dt>Promoter :</dt><dd>Ray Finn</dd>
    </dl>
    <div class="studio-mark">Cedar Hollow</div>
    <p class="studio-city">MILLBROOK KS 66402</p>
  </section>

  <section class="panel front-cover" aria-label="Front cover">
    <div class="front-art" role="img" aria-label="Empty church with rows of pews, the far wall opened onto a sunset meadow"></div>
    <h1 class="album-title">Beyond the<br>Orchard <span class="accent">Gate</span></h1>
    <p class="artist-name">Dale Harwick</p>
  </section>

  <section class="disc" aria-label="Disc label">
    <svg width="350" height="350" viewBox="0 0 350 350">
      <defs>
        <radialGradient id="disc-glow" cx="50%" cy="42%" r="40%">
          <stop offset="0" stop-color="#ffd36a"/>
          <stop offset="0.45" stop-color="#f2a03a"/>
          <stop offset="1" stop-color="#f2a03a" stop-opacity="0"/>
        </radialGradient>
        <linearGradient id="disc-art" x1="0" y1="0" x2="0" y2="1">
          <stop offset="0" stop-color="#1f0f2e"/>
          <stop offset="0.25" stop-color="#3a1a3c"/>
          <stop offset="0.52" stop-color="#e8782c"/>
          <stop offset="0.75" stop-color="#7a2a1e"/>
          <stop offset="1" stop-color="#2a1412"/>
        </linearGradient>
      </defs>
      <circle cx="175" cy="175" r="174" fill="var(--rim)" stroke="var(--rim-edge)" stroke-width="1.5"/>
      <g role="img" aria-label="Church and sunset meadow artwork printed on the disc">
        <circle cx="175" cy="175" r="169" fill="url(#disc-art)"/>
        <circle cx="175" cy="175" r="169" fill="url(#disc-glow)"/>
      </g>
      <circle cx="175" cy="175" r="32" fill="#f4f6f8" stroke="#9aa6b0" stroke-width="1"/>
      <circle cx="175" cy="175" r="22" fill="var(--stage)" stroke="#7d8790" stroke-width="1.5"/>
    </svg>
    <h2 class="disc-title">Beyond the<br>Orchard <span class="accent">Gate</span></h2>
    <p class="disc-catalog">14cd72RK-2</p>
    <p class="disc-artist">Dale Harwick</p>
  </section>

</body>
</html>
```